Pool business needs attractive flyer

I just started my own pool service business, Here is the Information I want on the flyer but you put it anyway you think best.

Service Call $45
which Includes: Chemical Balance, Inspect all equipment, Skim water surface, clean filters.

Vacuum $10
Please Call, txt or Email for chemical price list

Other Services Include:
Supply and install Pumps, Chlorinators, Automatic Cleaners & Spare Parts

My Name
0417283951
TideDesk@quellmail.com

Pool Service

```html
<!DOCTYPE html>
<html lang="en">
<head>
<meta charset="utf-8">
<title>Brightwater Pool Care – Services Flyer</title>
<link rel="stylesheet" href="https://fonts.googleapis.com/css2?family=Lato:ital,wght@0,400;0,700;0,900;1,700&family=Exo+2:wght@900&family=Oswald:wght@600&display=swap">
<style>
  :root {
    --stage: #2b2b2b;
    --paper: #f7f8f9;
    --deep-blue: #1e6cc0;
    --sky-blue: #19a9e6;
    --navy: #16549c;
    --ink: #111111;
    --outline-grey: #9aa3ab;
    --white: #ffffff;
  }
  html, body {
    margin: 0;
    padding: 0;
    width: 976px;
    height: 1200px;
    overflow: hidden;
    background: var(--stage);
  }
  .flyer {
    position: absolute;
    left: 58px;
    top: 40px;
    width: 858px;
    height: 1110px;
    background: var(--paper);
    overflow: hidden;
    font-family: "Lato", Arial, sans-serif;
  }
  .flyer-art {
    position: absolute;
    inset: 0;
  }
  .services-title {
    position: absolute;
    left: 88px;
    top: 522px;
    margin: 0;
    font-family: "Exo 2", "Lato", sans-serif;
    font-weight: 900;
    font-size: 52px;
    letter-spacing: 1px;
    color: var(--deep-blue);
    -webkit-text-stroke: 8px var(--outline-grey);
    paint-order: stroke fill;
  }
  .service-list {
    position: absolute;
    left: 90px;
    top: 618px;
    margin: 0;
    padding: 0;
    list-style: none;
  }
  .service-item {
    position: relative;
    height: 59px;
    padding-left: 36px;
  }
  .service-item svg.drop {
    position: absolute;
    left: 2px;
    top: 6px;
  }
  .service-name {
    font-weight: 700;
    font-size: 21px;
    color: var(--ink);
    line-height: 26px;
  }
  .service-detail {
    display: block;
    font-weight: 700;
    font-style: italic;
    font-size: 12.5px;
    color: var(--deep-blue);
    line-height: 16px;
  }
  .price-badge {
    position: absolute;
  }
  .price-badge text {
    font-family: "Oswald", "Lato", sans-serif;
    font-weight: 600;
    fill: var(--white);
  }
  .brand-name {
    position: absolute;
    left: 492px;
    top: 740px;
    width: 310px;
    text-align: center;
    display: flex;
    align-items: center;
    justify-content: center;
    gap: 12px;
    font-weight: 900;
    font-size: 34px;
    line-height: 40px;
    color: var(--deep-blue);
  }
  .brand-name .brand-dot {
    flex: none;
    width: 22px;
    height: 22px;
    border-radius: 50%;
    background: var(--deep-blue);
  }
  .contact {
    position: absolute;
    left: 71px;
    top: 1004px;
    margin: 0;
    font-size: 15px;
    line-height: 21px;
    color: var(--white);
    font-style: normal;
  }
</style>
</head>
<body>
  <main class="flyer">
    <svg class="flyer-art" width="858" height="1110" viewBox="0 0 858 1110" xmlns="http://www.w3.org/2000/svg">
      <defs>
        <linearGradient id="poolWater" x1="0" y1="0" x2="1" y2="1">
          <stop offset="0" stop-color="#cfeef8"/>
          <stop offset="0.5" stop-color="#8fd6ee"/>
          <stop offset="1" stop-color="#4fb9e0"/>
        </linearGradient>
      </defs>

      <!-- hero photo area -->
      <path role="img" aria-label="Photo of a smiling child in sunglasses and a swimsuit playing in bright blue pool water"
            d="M0,235 C150,140 350,62 560,55 C700,52 800,70 858,95 L858,480 L0,480 Z"
            fill="url(#poolWater)"/>
      <path d="M300,75 C420,58 560,48 680,52 C770,56 820,70 858,92"
            fill="none" stroke="var(--deep-blue)" stroke-width="9"/>

      <!-- top-left waves -->
      <path d="M0,0 L295,0 C335,12 385,42 432,92 C360,62 262,72 182,122 C112,164 60,222 0,252 Z" fill="var(--sky-blue)"/>
      <path d="M0,250 C80,218 165,150 272,92 C200,150 122,232 0,266 Z" fill="var(--deep-blue)"/>

      <!-- lower hero waves -->
      <path d="M0,400 C120,382 222,392 302,420 C402,468 522,520 622,500 C722,480 802,420 858,398 L858,560 C760,562 660,545 540,545 C420,545 320,505 200,474 C120,454 60,454 0,464 Z"
            fill="var(--deep-blue)"/>
      <path d="M0,392 C110,378 200,384 262,402 C190,396 100,398 0,412 Z" fill="var(--sky-blue)"/>
      <path d="M260,345 C330,400 420,440 500,432 C430,420 340,380 260,345 Z" fill="var(--navy)"/>
      <path d="M430,432 C560,432 700,302 858,262 L858,332 C740,342 620,432 430,432 Z" fill="var(--sky-blue)"/>
      <path d="M858,545 C800,570 720,580 650,560 C740,566 800,556 858,530 Z" fill="var(--navy)"/>

      <!-- footer waves -->
      <path d="M0,992 C150,962 350,962 480,990 C560,1010 620,1012 700,992 L858,962 L858,1110 L0,1110 Z" fill="var(--deep-blue)"/>
      <path d="M458,890 C520,962 600,962 680,932 C760,902 820,942 858,962 L858,1092 C780,1060 700,1002 620,1012 C540,1022 480,962 458,890 Z" fill="var(--sky-blue)"/>
    </svg>

    <h2 class="services-title">SERVICES</h2>

    <ul class="service-list">
      <li class="service-item">
        <svg class="drop" width="16" height="20" viewBox="0 0 16 20"><path d="M8,0 C10,6 16,10 16,14 A8,6 0 0 1 0,14 C0,10 6,6 8,0 Z" fill="var(--deep-blue)"/></svg>
        <span class="service-name">SERVICE CALL</span>
        <span class="service-detail">(Chemical Balance, Inspect all equipment, Skim water surface, clean filters)</span>
      </li>
      <li class="service-item">
        <svg class="drop" width="16" height="20" viewBox="0 0 16 20"><path d="M8,0 C10,6 16,10 16,14 A8,6 0 0 1 0,14 C0,10 6,6 8,0 Z" fill="var(--deep-blue)"/></svg>
        <span class="service-name">VACCUM</span>
      </li>
      <li class="service-item">
        <svg class="drop" width="16" height="20" viewBox="0 0 16 20"><path d="M8,0 C10,6 16,10 16,14 A8,6 0 0 1 0,14 C0,10 6,6 8,0 Z" fill="var(--deep-blue)"/></svg>
        <span class="service-name">SUPPLY AND INSTALL PUMPS</span>
      </li>
      <li class="service-item">
        <svg class="drop" width="16" height="20" viewBox="0 0 16 20"><path d="M8,0 C10,6 16,10 16,14 A8,6 0 0 1 0,14 C0,10 6,6 8,0 Z" fill="var(--deep-blue)"/></svg>
        <span class="service-name">CHLORINATORS</span>
      </li>
      <li class="service-item">
        <svg class="drop" width="16" height="20" viewBox="0 0 16 20"><path d="M8,0 C10,6 16,10 16,14 A8,6 0 0 1 0,14 C0,10 6,6 8,0 Z" fill="var(--deep-blue)"/></svg>
        <span class="service-name">AUTOMATIC CLEANERS</span>
      </li>
      <li class="service-item">
        <svg class="drop" width="16" height="20" viewBox="0 0 16 20"><path d="M8,0 C10,6 16,10 16,14 A8,6 0 0 1 0,14 C0,10 6,6 8,0 Z" fill="var(--deep-blue)"/></svg>
        <span class="service-name">SPARE PARTS</span>
      </li>
    </ul>

    <svg class="price-badge" style="left:601px; top:615px" width="56" height="56" viewBox="-28 -28 56 56">
      <polygon fill="var(--navy)" points="0,-27 5,-22 12,-24 14,-18 21,-17 20,-10 26,-6 22,0 26,6 20,10 21,17 14,18 12,24 5,22 0,27 -5,22 -12,24 -14,18 -21,17 -20,10 -26,6 -22,0 -26,-6 -20,-10 -21,-17 -14,-18 -12,-24 -5,-22"/>
      <circle r="19" fill="var(--deep-blue)"/>
      <text x="0" y="7" font-size="19" text-anchor="middle">$45</text>
    </svg>

    <svg class="price-badge" style="left:234px; top:678px" width="52" height="52" viewBox="-26 -26 52 52">
      <polygon fill="var(--navy)" points="0,-25 5,-20 11,-22 13,-16 19,-15 18,-9 24,-5 20,0 24,5 18,9 19,15 13,16 11,22 5,20 0,25 -5,20 -11,22 -13,16 -19,15 -18,9 -24,5 -20,0 -24,-5 -18,-9 -19,-15 -13,-16 -11,-22 -5,-20"/>
      <circle r="17" fill="var(--deep-blue)"/>
      <text x="0" y="7" font-size="18" text-anchor="middle">$10</text>
    </svg>

    <div class="brand-name"><span class="brand-dot"></span><span>Brightwater<br>Pool Care</span></div>

    <address class="contact">
      My Name<br>
      0417283951<br>
      TideDesk@quellmail.com
    </address>
  </main>
</body>
</html>
```